New Business Card Design Project

Make a kick ass business card for The Otter Tea Mug, using the designs. I also might like the 2nd place design logo on the back? Maybe all black with that? Not sure. Also, I'm cool with it being on metal, plastic, glass? or whatever for the business card. Maybe shaped like a shark? Let me know what else you need? Would like designs in the next day or so. Thank you.
Target Market(s)
Anyone that is cool
Contact Information for Business Card
Name: Dorian Fenwick
Phone: 317.594.8126
inventor/creator/entrepreneur/owner
www.theottertyeamug.example
social media links
https://www.facebook.com/theottertyeamug
https://twitter.com/otter_brew
https://www.instagram.com/theottertyeamug/
I'll get the Pinterest one soon
Colors
Designer to choose colors to be used in the design.
Requirements
Must have
- The Otter Tea Mug
- www.theottertyeamug.example
- social media tags?
- My logos and picture/photo of wine glass
Nice to have
- Maybe shaped like a wine glass or shark
- I'll let you decide but my same colors from my website would be nice

```html
<!DOCTYPE html>
<html lang="en">
<head>
<meta charset="utf-8">
<title>The Otter Tea Mug – Business Card</title>
<link rel="stylesheet" href="https://fonts.googleapis.com/css2?family=Lato:wght@300;400;700&display=swap">
<style>
  :root {
    --backdrop: #4b4b4b;
    --card-white: #ffffff;
    --brand-red: #c0272d;
    --brand-red-soft: #e7a3a5;
    --ink: #1d1d1d;
    --logo-light: #f3e9e9;
  }
  * { box-sizing: border-box; margin: 0; padding: 0; }
  html, body {
    width: 1200px; height: 1056px; overflow: hidden;
    background: var(--backdrop);
    font-family: "Lato", sans-serif;
  }
  .stage { position: relative; width: 1200px; height: 1056px; }

  .card {
    position: absolute; top: 228px;
    width: 344px; height: 600px;
    overflow: hidden;
  }
  .card--front { left: 236px; background: var(--card-white); }
  .card--back  { left: 622px; background: var(--brand-red); }

  .holder-name {
    position: absolute; top: 56px; left: 0; width: 100%;
    text-align: center; color: var(--brand-red);
    font-weight: 700; font-size: 27px; letter-spacing: 0.5px;
  }
  .holder-role {
    position: absolute; top: 90px; left: 0; width: 100%;
    text-align: center; color: var(--ink);
    font-size: 16px;
  }

  .glass-art {
    position: absolute; left: 184px; top: 132px;
    width: 160px; height: 468px;
    background: linear-gradient(180deg, #fbeeee 0%, var(--brand-red-soft) 40%, #f7e1e2 75%, var(--card-white) 100%);
    border-radius: 160px 0 0 0;
  }

  .contact-list { position: absolute; left: 0; top: 0; width: 100%; height: 100%; list-style: none; }
  .contact-item {
    position: absolute; left: 46px;
    display: flex; align-items: center; gap: 8px;
    font-size: 16px; color: var(--ink);
  }
  .contact-icon { width: 20px; height: 20px; flex: none; }
</style>
</head>
<body>
<main class="stage">

  <section class="card card--front" aria-label="Card front">
    <h1 class="holder-name">DORIAN FENWICK</h1>
    <p class="holder-role">inventor/creator/entrepreneur/owner</p>

    <div class="glass-art" role="img" aria-label="Red tea mug illustration with the brand mark inside"></div>

    <ul class="contact-list">
      <li class="contact-item" style="top:392px">
        <svg class="contact-icon" viewBox="0 0 20 20"><circle cx="10" cy="10" r="9" fill="none" stroke="#c0272d" stroke-width="1.4"/><path d="M6.5 5.5l2 0 1 2.5-1.3 1c.7 1.4 1.5 2.2 2.8 2.8l1-1.3 2.5 1v2c-4.5.3-8.3-3.5-8-8z" fill="#c0272d"/></svg>
        <span>317.594.8126</span>
      </li>
      <li class="contact-item" style="top:418px">
        <svg class="contact-icon" viewBox="0 0 20 20"><circle cx="10" cy="10" r="9" fill="none" stroke="#c0272d" stroke-width="1.4"/><circle cx="10" cy="10" r="5" fill="none" stroke="#c0272d" stroke-width="1.3"/><ellipse cx="10" cy="10" rx="2" ry="5" fill="none" stroke="#c0272d" stroke-width="1.1"/><path d="M5 10h10" stroke="#c0272d" stroke-width="1.1"/></svg>
        <span>www.theottertyeamug.example</span>
      </li>
      <li class="contact-item" style="top:462px">
        <svg class="contact-icon" viewBox="0 0 20 20"><circle cx="10" cy="10" r="9" fill="none" stroke="#c0272d" stroke-width="1.4"/></svg>
        <span>theottertyeamug</span>
      </li>
      <li class="contact-item" style="top:488px">
        <svg class="contact-icon" viewBox="0 0 20 20"><circle cx="10" cy="10" r="9" fill="none" stroke="#c0272d" stroke-width="1.4"/></svg>
        <span>theottertyeamug</span>
      </li>
      <li class="contact-item" style="top:514px">
        <svg class="contact-icon" viewBox="0 0 20 20"><circle cx="10" cy="10" r="9" fill="none" stroke="#c0272d" stroke-width="1.4"/></svg>
        <span>otter_brew</span>
      </li>
      <li class="contact-item" style="top:540px">
        <svg class="contact-icon" viewBox="0 0 20 20"><circle cx="10" cy="10" r="9" fill="none" stroke="#c0272d" stroke-width="1.4"/></svg>
        <span>theottertyeamug</span>
      </li>
    </ul>
  </section>

  <section class="card card--back" aria-label="Card back">
    <p style="position:absolute;top:334px;left:0;width:100%;text-align:center;color:var(--logo-light);font-weight:300;font-size:26px;">TheOtterTeaMug</p>
  </section>

</main>
</body>
</html>
```